Ashworth Web Design Project

I need the front page and an internal page designed for this client's website. The logo is attached. Obviously the colors have to go with and/or work with the logo colors. I also attached a very rough brochure layout to help you see the direction we're going in with print materials. The rough site map is also attached. I see a slider on the homepage, the art for which I may come back to you to create. This clinic is in a very high end Dallas neighborhood. The hook is that it's a primary care and urgent facility with convenient hours.

I don't know how much this impacts your design, but this will be a Wordpress site and I'm using a framework called Struxo (struxo-demo.example). If Struxo proves to be inflexible, I'll have to get a template that allows me to execute your design.

This site (http://oakbendcareclinic.example) has the type and quality of content I will eventually have on the Ashworth site.

I just revised the brief for this project. I added the site map and added details to the overview and the "Must Have" section. Thank you for revisiting the brief. 

Reason: Christmas was a bad time to end it.

Target Market(s)

Women 25-54 with children living at home, income over $150k/year

Industry/Entity Type

Clinic

Requirements
Must have
• Masthead incorporating the logo
Followed by the primary nav
Slider on the home page below that
Dual nav - 1 with the nav in the attached site map
2 secondary nav with areas of healthcare
There will three blocks under the nav
1. It's about time (with a small blurb less than 50 words.
2. It's about choices (with small blurb)
3. It's about you (with small blurb)
Three footer blocks
patient check in link on every page
"No appointment? No problem" icon on every page

```html
<!DOCTYPE html>
<html lang="en">
<head>
<meta charset="utf-8">
<title>Ashworth Medical</title>
<link href="https://fonts.googleapis.com/css2?family=Open+Sans:wght@400;600;700&family=Arimo:wght@400;700&display=swap" rel="stylesheet">
<style>
:root{
  --green:#3aa41c;--green-dark:#238a0c;--blue:#2f6fc4;--blue-dark:#1f55a3;
  --ink:#444;--muted:#666;--line:#e2e4e8;--page:#f3f5f8;--dark:#2b2f36;--darker:#1f2227;
}
*{margin:0;padding:0;box-sizing:border-box}
html,body{width:1094px;height:1200px;overflow:hidden}
body{background:var(--page);font-family:Arimo,Arial,sans-serif;color:var(--ink);position:relative}
.abs{position:absolute}
.topbar{left:0;top:0;width:1094px;height:22px;background:var(--darker);color:#ddd;font-size:11px}
.follow{left:144px;top:5px;display:flex;gap:5px;align-items:center}
.follow i{display:inline-block;width:13px;height:13px;border-radius:2px}
.toplinks{right:120px;top:5px;display:flex;gap:30px;font-weight:700;color:#fff}
.sheet{left:24px;top:22px;width:1010px;height:958px;background:#fff}
.logo{left:138px;top:36px;display:flex;align-items:center;gap:8px}
.logo .mark{width:48px;height:48px;border-radius:50%;background:var(--blue)}
.logo .name{font-family:"Open Sans",sans-serif;font-weight:700;font-size:31px;color:var(--blue);letter-spacing:-.5px}
.tagline{left:196px;top:76px;font-size:11px;font-weight:700;color:#555;border-top:1px solid #555;border-bottom:1px solid #555;padding:0 4px}
.cta{top:42px;height:47px;border-radius:4px;color:#fff;display:flex;align-items:center;gap:10px;padding:0 14px;font-family:"Open Sans",sans-serif;font-weight:700}
.cta.walkin{left:608px;width:171px;background:linear-gradient(#4cb62b,#1f8a0d);font-size:14px;line-height:16px}
.cta.check{left:786px;width:172px;background:linear-gradient(#4d8ad8,#1f58a8);font-size:17px}
.mainnav{left:137px;top:108px;width:821px;height:42px;background:linear-gradient(#fff,#eceef1);border:1px solid #dadde2;display:flex;box-shadow:0 3px 4px rgba(0,0,0,.12)}
.mainnav a{flex:auto;display:flex;align-items:center;justify-content:center;font-family:"Open Sans",sans-serif;font-size:11.5px;color:#333;border-right:1px solid #dadde2;text-decoration:none}
.mainnav a.current{background:linear-gradient(#3fae1e,#23890d);color:#fff;flex:0 0 84px}
.areas{left:137px;top:168px;width:187px;height:256px;background:linear-gradient(#3f7fd0,#2a66b8);border-radius:4px}
.areas h2{height:36px;display:flex;align-items:center;gap:10px;padding-left:10px;color:#fff;font-family:"Open Sans",sans-serif;font-size:14.5px;font-weight:600;background:var(--blue-dark);border-radius:4px 4px 0 0}
.areas li{list-style:none;height:30px;border-bottom:1px solid rgba(255,255,255,.2);color:#fff;font-size:12px;display:flex;align-items:center;padding-left:12px;letter-spacing:.2px}
.areas li::before{content:"›";margin-right:6px;font-size:15px}
.block{left:137px;width:187px;background:#f0f1f3}
.block h3{height:34px;background:linear-gradient(#45b424,#23890d);color:#fff;font-family:"Open Sans",sans-serif;font-size:14.5px;font-weight:600;display:flex;align-items:center;gap:8px;padding-left:8px}
.block p{padding:10px 8px;font-size:10.5px;line-height:15.5px;color:var(--muted)}
.block b{color:#555}
.slider{left:338px;top:168px;width:620px;height:278px}
.photo{position:absolute;border:1px solid #ddd}
.front{left:100px;top:46px;width:428px;height:234px;background:#fff;border-radius:4px;box-shadow:0 2px 6px rgba(0,0,0,.25);padding:10px}
.front .photo{position:static;width:100%;height:100%;background:linear-gradient(120deg,#e8ecef,#c9b6a4 55%,#8fa4c2)}
.dots{left:627px;top:457px;display:flex;gap:4px}
.dots i{width:11px;height:11px;border-radius:50%;border:1px solid #bbb;background:#fff}
.dots i.on{background:var(--blue);border-color:var(--blue)}
.welcome{left:338px;top:480px;width:620px;height:168px;background:linear-gradient(#f5f6f8,#fff 40px)}
.welcome h1{position:absolute;left:22px;top:12px;font-family:"Open Sans",sans-serif;font-size:20px;font-weight:600;color:var(--green);display:flex;align-items:center;gap:10px}
.welcome h1 span{color:var(--blue-dark)}
.globe{width:26px;height:26px;border-radius:50%;background:var(--blue);display:inline-block}
.welcome .rule{position:absolute;left:22px;top:50px;width:590px;border-top:1px dashed #ccc}
.welcome p{position:absolute;left:20px;top:62px;width:582px;font-size:10.5px;line-height:16px;color:#555}
.more{font-size:10.5px;font-weight:700;color:var(--green-dark);display:flex;align-items:center;gap:4px}
.more::before{content:"+";width:12px;height:12px;border-radius:50%;background:var(--green);color:#fff;font-size:11px;line-height:12px;text-align:center}
.services{left:356px;top:666px;width:586px;height:286px;border:1px solid #d9dce0;border-radius:6px;background:#fff;display:flex;padding:12px 10px;gap:15px}
.service{width:180px}
.service h4{font-family:"Open Sans",sans-serif;font-size:13.5px;font-weight:600;color:var(--green);display:flex;align-items:center;gap:6px;height:26px}
.service h4 span{color:var(--blue-dark)}
.service .globe{width:19px;height:19px}
.service .img{height:108px;margin:10px 0 14px;border:1px solid #ccc}
.service p{font-size:10.5px;line-height:15.5px;color:var(--muted);padding:0 4px;height:90px}
.service b{color:#555}
.footer{left:0;top:980px;width:1094px;height:186px;background:var(--dark);border-top:3px solid #4d7ab8;color:#ccc}
.footer h5{position:absolute;top:14px;font-family:"Open Sans",sans-serif;font-size:15px;font-weight:400;color:#fff;padding-bottom:8px;border-bottom:1px solid #555;width:230px}
.links{position:absolute;top:52px;font-size:10.5px;width:108px}
.links li{list-style:none;height:26px;border-bottom:1px solid #3b4049;display:flex;align-items:center;padding-left:8px}
.links li::before{content:"";border-left:6px solid var(--green);border-top:4px solid transparent;border-bottom:4px solid transparent;margin-right:12px}
.links li.active{background:#1b1e22}
.news p{position:absolute;left:463px;top:52px;width:210px;font-size:10.5px;line-height:16px}
.email{left:463px;top:1082px;width:174px;height:30px;background:#fff;border-radius:3px;color:#bbb;font-size:10.5px;display:flex;align-items:center;gap:8px;padding-left:8px}
.subscribe{left:463px;top:1130px;width:84px;height:24px;background:linear-gradient(#3fae1e,#1f850b);color:#fff;font-family:"Open Sans",sans-serif;font-weight:700;font-size:11px;display:flex;align-items:center;justify-content:center;border-radius:2px}
.contact{position:absolute;left:740px;font-size:10.5px;line-height:13px;display:flex;gap:14px;align-items:flex-start}
.bottombar{left:0;top:1166px;width:1094px;height:34px;background:#fff;font-size:10.5px;color:#333;display:flex;align-items:center;justify-content:center;gap:10px}
</style>
</head>
<body>
<div class="abs sheet"></div>
<div class="abs topbar">
  <div class="abs follow">Follow Us <i style="background:#5aa7d8"></i><i style="background:#3d5a98"></i><i style="background:#c4302b"></i></div>
  <div class="abs toplinks"><span>Register</span><span>Log In</span><span>Blog</span></div>
</div>

<header>
  <div class="abs logo"><span class="mark"></span><span class="name">AshworthMedical</span></div>
  <div class="abs tagline">Immediate Family and Personal Care</div>
  <a class="abs cta walkin"><svg width="26" height="24" viewBox="0 0 26 24"><path d="M13 2 25 22H1Z" fill="#fff"/><rect x="11.8" y="8" width="2.4" height="8" fill="#2d9815"/><rect x="11.8" y="17.5" width="2.4" height="2.4" fill="#2d9815"/></svg><span>No appointment?<br>No problem</span></a>
  <a class="abs cta check"><svg width="22" height="22"><rect width="22" height="22" rx="2" fill="#fff"/><path d="M9 4h4v5h5v4h-5v5H9v-5H4V9h5z" fill="#2f6fc4"/></svg>Patient Check</a>
  <nav class="abs mainnav">
    <a class="current">HOME</a><a>ABOUT US</a><a>SERVICES</a><a>STAFF</a><a>INSURANCE</a><a>SCHOLARSHIPS</a><a>VIDEOS</a><a>CONTACT US</a>
  </nav>
</header>

<aside>
  <div class="abs areas">
    <h2><svg width="20" height="20"><path d="M7 0h6v7h7v6h-7v7H7v-7H0V7h7z" fill="#fff"/></svg>Areas Of Healthcare</h2>
    <ul><li>IMMEDIATE CARE</li><li>ALLERGIES</li><li>PRIMARY CARE</li><li>WOMEN'S HEALTH</li><li>MEDICAL SPA TREATMENTS</li><li>MEN'S HEALTH</li><li>WEIGHT LOSS</li></ul>
  </div>
  <section class="abs block" style="top:434px;height:202px">
    <h3><svg width="24" height="24"><circle cx="12" cy="13" r="9" fill="none" stroke="#fff" stroke-width="2.5"/><path d="M12 8v5h4" stroke="#fff" stroke-width="2" fill="none"/></svg>It's About Time</h3>
    <p><b>Lorem ipsum dolor sit amet</b><br>consectetuer adipiscing elit, sed iam nonummy nibh euismod tincidunt ut laoreet dolore magna aliquam erat volutpat.Ut wisi enim ad minim niam, quis nostrud exeilLorem ipsum olor sit ametconsectetuer adipiscing elit, sed iam nonummy nibh euismod nnt ut laoreet dolore magna aliquam Aat volutpat.Ut wisi enim ad minim</p>
  </section>
  <section class="abs block" style="top:653px;height:145px">
    <h3><svg width="24" height="24"><circle cx="12" cy="12" r="10" fill="none" stroke="#fff" stroke-width="2.5"/><text x="12" y="17" text-anchor="middle" fill="#fff" font-size="14" font-weight="700" font-family="Arial,sans-serif">?</text></svg>It's About Choices</h3>
    <p><b>Lorem ipsum dolor sit amet</b><br>consectetuer adipiscing elit, sed iam nonummy nibh euismod tincidunt ut laoreet dolore magna aliquam erat volutpat.Ut wisi enim ad minim niam, quis nostrud exe.</p>
  </section>
  <section class="abs block" style="top:809px;height:145px">
    <h3><svg width="34" height="20"><path d="M2 6h6v12H2zM10 7l8-5 2 2-4 4h14a2 2 0 0 1 0 4H20v1h-6v2h-4z" fill="none" stroke="#fff" stroke-width="2"/></svg>It's About You</h3>
    <p><b>Lorem ipsum dolor sit amet</b><br>consectetuer adipiscing elit, sed iam nonummy nibh euismod tincidunt ut laoreet dolore magna aliquam erat volutpat.Ut wisi enim ad minim niam, quis nostrud exe.</p>
  </section>
</aside>

<main>
  <div class="abs slider">
    <div class="photo" role="img" aria-label="Smiling nurse with stethoscope" style="left:10px;top:12px;width:110px;height:216px;background:linear-gradient(#e9ecee,#b9c9d6)"></div>
    <div class="photo" role="img" aria-label="Doctor caring for an elderly patient" style="left:498px;top:12px;width:112px;height:216px;background:linear-gradient(#f1ecea,#d9c2c7)"></div>
    <div class="photo front" style="border:0"><div class="photo" role="img" aria-label="Doctor and nurse welcoming a young family"></div></div>
  </div>
  <div class="abs dots"><i></i><i class="on"></i><i></i></div>

  <section class="abs welcome">
    <h1><i class="globe"></i>Welcome To <span>Ashworth Medical</span></h1>
    <div class="rule"></div>
    <p>Lorem ipsum dolor sit amet, consectetuer adipiscing elit, sed diam nonummy nibh euismod tincidunt ut laoreet dolore magna aliquam erat volutpat. Ut wisi enim ad minim veniam, quis nostrud exerci tation ullamcorper suscipit lobortis nisl ut aliquip ex ea commodo consequat. Duis autem vel eum iriure dolor in hendrerit in vulputate velit esse molestie consequat, vel illum dolore eu feugiat nulla facilisis at vero eros et accumsan et iusto odio dignissim qui blandit praesent luptatum zzril delenit augue duis dolore te feugait nulla facilisi.</p>
    <span class="abs more" style="left:530px;top:138px">Read More</span>
  </section>

  <section class="abs services">
    <article class="service">
      <h4><i class="globe"></i>Primary <span>Care</span></h4>
      <div class="img" role="img" aria-label="Parent taking a child's temperature" style="background:linear-gradient(135deg,#d9a9b8,#c7b07f)"></div>
      <p><b>Lorem ipsum dolor sit amet</b><br>consectetuer adipiscing elit, sed iam nonummy nibh euismod tincidunt ut laoreet dolore magna aliquam erat volutpat.Ut wisi enim.</p>
      <span class="more" style="color:#666">Read More</span>
    </article>
    <article class="service">
      <h4><i class="globe"></i>Immediate <span>Care</span></h4>
      <div class="img" role="img" aria-label="Paramedics attending to a patient" style="background:linear-gradient(135deg,#8a6a3a,#3c3a3a 60%,#b24a2a)"></div>
      <p><b>Lorem ipsum dolor sit amet</b><br>consectetuer adipiscing elit, sed iam nonummy nibh euismod tincidunt ut laoreet dolore magna aliquam erat volutpat.Ut wisi enim .</p>
      <span class="more" style="color:#666">Read More</span>
    </article>
    <article class="service">
      <h4><i class="globe"></i>Medical <span>Spa Treatments</span></h4>
      <div class="img" role="img" aria-label="Client receiving a spa treatment" style="background:linear-gradient(135deg,#dfe4ea,#a9b3bf)"></div>
      <p><b>Lorem ipsum dolor sit amet</b><br>consectetuer adipiscing elit, sed iam nonummy nibh euismod tincidunt ut laoreet dolore magna aliquam erat volutpat.Ut wisi enim.</p>
      <span class="more" style="color:#666">Read More</span>
    </article>
  </section>
</main>

<footer class="abs footer">
  <h5 style="left:138px">Quick Links</h5>
  <ul class="links" style="left:138px"><li>Home</li><li class="active">About Us</li><li>Services</li><li>Staff</li><li>Insurance</li></ul>
  <ul class="links" style="left:262px;width:108px"><li>Scholarships</li><li>Videos</li><li>Contact Us</li><li>Site Map</li><li>Terms of Service</li></ul>
  <div class="news"><h5 style="left:463px;width:185px">Newsletter</h5>
  <p>Get updates about promotions and new products by entering e-mail</p></div>
  <h5 style="left:742px;width:185px">Contact Details</h5>
  <div class="contact" style="top:52px"><svg width="18" height="16"><path d="M9 0 18 8h-3v8H3V8H0Z" fill="#fff"/></svg><span>Donec et nibh mauris. nibh<br>varius at euismod risus eleifend.</span></div>
  <div class="contact" style="top:91px"><svg width="18" height="18"><circle cx="9" cy="9" r="8" fill="none" stroke="#fff" stroke-width="1.5"/><path d="M6 5c0 5 2 7 6 8" stroke="#fff" stroke-width="2" fill="none"/></svg><span style="line-height:18px">555.014.2210</span></div>
  <div class="contact" style="top:120px"><svg width="18" height="18"><text x="9" y="15" text-anchor="middle" fill="#fff" font-size="17" font-family="Arial,sans-serif">@</text></svg><span style="line-height:18px">info@ashworthmedical.example</span></div>
</footer>
<div class="abs email"><svg width="20" height="14"><rect x="1" y="1" width="18" height="12" fill="none" stroke="#bbb"/><path d="M1 1l9 7 9-7" fill="none" stroke="#bbb"/></svg>your e-mail address</div>
<div class="abs subscribe">Subscribe</div>

<div class="abs bottombar"><span>©2012. Ashworth Medical. All right reserved.</span><span>|</span><span>Privacy Policy</span></div>
</body>
</html>
```